2-Sided Flyer for Printing - Quarvelent

We are looking for the most attractive and best quality flyer to serve as a handout to distribute as a printed document in fairs and conventions. We want one A4 sheet using two sides to display what is Quarvelent in an attractive and simple way.
• What is Quarvelent, what we do and benefits
o Type of challenges we solve
o Benefit for the companies
o Benefit for the solvers (engineers)
• How does it work
• Sample challenges
• Show our Community (skills, solvers pictures, etc)
The flyer should be developed according to our corporate colours (see landing page and logo)
The material we are uploading is the following:
• Power point with the introduction to Quarvelent
• Sample non professional flyers
• In addition you can use any material available through our web: www.quarvelent-example.com (landing page, blog, clients pages, ranking, etc.)

Target Market(s)

industrial companies and engineers

Industry/Entity Type

Engineering

Requirements
Must have
• A single flyer to be used for companies (clients) and engineers (solvers)
• overall flyer creative design
• clear and clean messages
• contain what is Quarvelent, how it works, community and sample challenges
• social networks info
• corporate pallet
Nice to have
• attractive funnel design to show how to move from a challenge to unique solutions
• attractive way to show the crowd using real solvers pictures
• Not all the background should be coloured (combination of white and corporate colours)
Should not have
• Copy and paste of the provided information and pictures
• High density content
• We do not like the design of the file "Brochure OK final.pdf" and we are looking for a 2-sided flyer

```html
<!DOCTYPE html>
<html lang="en">
<head>
<meta charset="utf-8">
<title>Quarvelent – Two-Sided Flyer</title>
<link rel="stylesheet" href="https://fonts.googleapis.com/css2?family=Oswald:wght@500;600&family=Open+Sans:wght@400;600&display=swap">
<style>
:root{
  --stage:#2b2b2d;
  --paper:#ffffff;
  --blue:#29a8e0;
  --blue-deep:#1f78bf;
  --green:#1aa98a;
  --orange-red:#f15a29;
  --orange:#eea435;
  --red:#e6252b;
  --lime:#c5d52a;
  --ink:#333333;
  --muted:#555555;
  --dark-panel:#333335;
  --band-a:#4f7296;
  --band-b:#8ca4bd;
}
*{box-sizing:border-box;margin:0;padding:0}
html,body{width:1200px;height:960px;overflow:hidden}
body{background:var(--stage);font-family:'Open Sans',Arial,sans-serif;color:var(--ink);position:relative}
.flyer{position:absolute;top:122px;width:543px;height:768px;background:var(--paper);overflow:hidden}
.flyer--front{left:44px}
.flyer--back{left:614px}
.abs{position:absolute}
.heading{font-family:'Oswald','Arial Narrow',sans-serif;font-weight:500;text-transform:uppercase;white-space:nowrap}
.tab{position:absolute;left:0;height:24px;color:#fff;font-family:'Oswald','Arial Narrow',sans-serif;font-weight:500;font-size:14px;line-height:24px;padding:0 8px 0 30px;text-transform:uppercase;white-space:nowrap}
.hex{position:absolute;clip-path:polygon(25% 0,75% 0,100% 50%,75% 100%,25% 100%,0 50%)}
.hex-label{position:absolute;width:90px;margin-left:-45px;text-align:center;font-size:8px;line-height:9px;color:var(--muted)}
.hex-label--light{color:#fff;font-weight:600}
/* front header */
.front-header{left:0;top:0;width:543px;height:134px;background:linear-gradient(180deg,#f4f8fb,#e8f0f6)}
.front-header__panel{left:0;top:0;width:543px;height:134px;background:var(--blue);clip-path:polygon(268px 0,543px 0,543px 134px,240px 134px)}
.brand{font-size:30px;font-weight:400;color:var(--ink);letter-spacing:.5px;white-space:nowrap}
.brand-dot{display:inline-block;width:14px;height:14px;border-radius:50%;background:var(--blue);margin-right:8px;vertical-align:middle}
.intro-list{left:272px;top:24px;width:262px;list-style:none;color:#fff;font-size:11px;line-height:14.5px}
.intro-list li{margin-bottom:7px;padding-left:10px;position:relative}
.intro-list li::before{content:"•";position:absolute;left:0}
/* challenge band */
.challenge-band{left:0;top:138px;width:543px;height:197px;background:linear-gradient(160deg,var(--band-b),var(--band-a))}
.challenge-frame{left:10px;top:15px;width:524px;height:172px;border:1.5px solid #fff}
.challenge-title{left:0;top:8px;width:543px;text-align:center;color:#fff;font-size:20px}
.challenge-title span{padding:0 6px}
/* benefits */
.benefit-list{list-style:none;position:absolute;left:34px;width:232px;font-size:10px;line-height:13px;color:var(--muted)}
.benefit-list li{position:relative;padding-left:14px;margin-bottom:5px}
.benefit-list svg{position:absolute;left:0;top:2px}
/* funnel */
.funnel-title{width:200px;text-align:center;font-size:17px}
.art-strip{left:0;width:543px;height:102px;background:linear-gradient(90deg,#f2c9a0,#e8a0a8 30%,#f4d36a 55%,#8fc6e8 75%,#f08f7a)}
/* back */
.back-bg{left:0;top:0;width:543px;height:200px;background:linear-gradient(160deg,#e3eef8,#fff 70%)}
.challenge-kicker{left:30px;top:50px;font-size:14px;line-height:16px;text-transform:none;color:var(--ink)}
.qtext{left:30px;top:68px;width:240px;font-size:13.5px;line-height:18.5px;color:var(--ink)}
.sub-title{font-size:16px;color:var(--blue-deep);font-weight:600}
.hex-wrap{position:absolute;clip-path:polygon(25% 0,75% 0,100% 50%,75% 100%,25% 100%,0 50%);background:var(--green)}
.community{left:0;top:486px;width:543px;height:166px;background:var(--dark-panel)}
.member{position:absolute;width:150px;margin-left:-75px;text-align:center;color:#fff}
.member__photo{width:88px;height:88px;border-radius:50%;border:3px solid #fff;margin:0 auto;background:linear-gradient(160deg,#9fb4c8,#5d6b78)}
.member__name{font-size:15px;font-weight:400;margin-top:8px}
.member__role{font-size:11.5px;margin-top:1px}
.divider{position:absolute;width:1.5px;background:#d8d8d8;top:26px;height:124px}
</style>
</head>
<body>

<section class="flyer flyer--front">
  <div class="abs front-header"></div>
  <div class="abs front-header__panel"></div>
  <div class="abs brand" style="left:44px;top:48px"><span class="brand-dot"></span>Quarvelent</div>
  <ul class="abs intro-list">
    <li>Helps companies solve engineering challenges through online contests</li>
    <li>Our proprietary platform helps finding amazing viable solutions to complex challenges</li>
    <li>We run on-line competitions through our proprietary platform</li>
  </ul>

  <div class="abs challenge-band" role="img" aria-label="Engineer working on industrial site, background photo">
    <div class="abs challenge-frame"></div>
    <div class="abs heading challenge-title"><span style="background:#6c88a6">Type of challenges we solve</span></div>
  </div>
  <div class="hex" style="left:24px;top:218px;width:64px;height:58px;background:#8aa3b8" role="img" aria-label="Cooling tower photo"></div>
  <div class="hex" style="left:87px;top:196px;width:64px;height:58px;background:#7a8f86" role="img" aria-label="Instrumentation plant photo"></div>
  <div class="hex" style="left:149px;top:218px;width:64px;height:58px;background:#a7b2bd" role="img" aria-label="Factory roof photo"></div>
  <div class="hex" style="left:210px;top:192px;width:64px;height:58px;background:#9ab0c0" role="img" aria-label="Wind turbines photo"></div>
  <div class="hex" style="left:272px;top:218px;width:64px;height:58px;background:#c9a63a" role="img" aria-label="Mining vehicle photo"></div>
  <div class="hex" style="left:333px;top:196px;width:64px;height:58px;background:#a0673e" role="img" aria-label="Industrial infrastructure photo"></div>
  <div class="hex" style="left:394px;top:218px;width:64px;height:58px;background:#7e6a4c" role="img" aria-label="Workers with machinery photo"></div>
  <div class="hex" style="left:456px;top:196px;width:64px;height:58px;background:#6e8e74" role="img" aria-label="Solar panel house photo"></div>
  <div class="hex-label hex-label--light" style="left:56px;top:290px">Water and<br>Energy</div>
  <div class="hex-label hex-label--light" style="left:119px;top:264px">Instrumentation</div>
  <div class="hex-label hex-label--light" style="left:181px;top:290px">Sustainability</div>
  <div class="hex-label hex-label--light" style="left:242px;top:264px">Logistics<br>costs</div>
  <div class="hex-label hex-label--light" style="left:304px;top:290px">Extreme<br>environment</div>
  <div class="hex-label hex-label--light" style="left:365px;top:264px">Infrastructure<br>costs</div>
  <div class="hex-label hex-label--light" style="left:426px;top:290px">Labor<br>Productivity</div>
  <div class="hex-label hex-label--light" style="left:488px;top:264px">Internet<br>of Things (IoT)</div>

  <div class="tab" style="top:355px;min-width:194px;background:var(--orange-red)">Benefit for the companies</div>
  <ul class="benefit-list" style="top:392px">
    <li><svg width="9" height="9"><rect x=".5" y=".5" width="8" height="8" fill="none" stroke="#29a8e0"/><path d="M2 4.5l2 2 4-5" stroke="#29a8e0" fill="none" stroke-width="1.3"/></svg>Be more competitive through product and process innovation</li>
    <li><svg width="9" height="9"><rect x=".5" y=".5" width="8" height="8" fill="none" stroke="#29a8e0"/><path d="M2 4.5l2 2 4-5" stroke="#29a8e0" fill="none" stroke-width="1.3"/></svg>Deliver better innovation results through better solutions</li>
    <li><svg width="9" height="9"><rect x=".5" y=".5" width="8" height="8" fill="none" stroke="#29a8e0"/><path d="M2 4.5l2 2 4-5" stroke="#29a8e0" fill="none" stroke-width="1.3"/></svg>Reduce uncertainties when adopting new technologies</li>
    <li><svg width="9" height="9"><rect x=".5" y=".5" width="8" height="8" fill="none" stroke="#29a8e0"/><path d="M2 4.5l2 2 4-5" stroke="#29a8e0" fill="none" stroke-width="1.3"/></svg>Increase capacity of internal engineering teams</li>
  </ul>

  <div class="tab" style="top:510px;min-width:251px;background:var(--orange)">Benefit for the solvers</div>
  <ul class="benefit-list" style="top:547px">
    <li><svg width="9" height="9"><rect x=".5" y=".5" width="8" height="8" fill="none" stroke="#e6252b"/><path d="M2 4.5l2 2 4-5" stroke="#e6252b" fill="none" stroke-width="1.3"/></svg>Connect with broader talent and experience from a global and diverse engineering community</li>
    <li><svg width="9" height="9"><rect x=".5" y=".5" width="8" height="8" fill="none" stroke="#e6252b"/><path d="M2 4.5l2 2 4-5" stroke="#e6252b" fill="none" stroke-width="1.3"/></svg>Bring innovations from other industries</li>
    <li><svg width="9" height="9"><rect x=".5" y=".5" width="8" height="8" fill="none" stroke="#e6252b"/><path d="M2 4.5l2 2 4-5" stroke="#e6252b" fill="none" stroke-width="1.3"/></svg>Enhance internal innovation culture looking outside</li>
    <li><svg width="9" height="9"><rect x=".5" y=".5" width="8" height="8" fill="none" stroke="#e6252b"/><path d="M2 4.5l2 2 4-5" stroke="#e6252b" fill="none" stroke-width="1.3"/></svg>Extend the supplier network with a broader perspective</li>
  </ul>

  <div class="abs heading funnel-title" style="left:306px;top:360px;color:var(--orange-red)">Challenge</div>
  <svg class="abs" style="left:300px;top:385px" width="240" height="245" viewBox="0 0 240 245" aria-label="Funnel from challenge to unique solutions">
    <path d="M-10 33 L100 238 M250 33 L140 238" stroke="#777" stroke-dasharray="1.5 2.5" fill="none"/>
    <g fill="#e6252b">
      <circle cx="76" cy="15" r="2.4"/><circle cx="88" cy="8" r="2"/><circle cx="100" cy="20" r="2.4"/><circle cx="110" cy="6" r="2"/><circle cx="118" cy="26" r="2.4"/><circle cx="128" cy="14" r="2"/><circle cx="138" cy="24" r="2.4"/><circle cx="146" cy="10" r="2"/><circle cx="152" cy="30" r="2.4"/><circle cx="92" cy="30" r="2"/><circle cx="106" cy="38" r="2.4"/><circle cx="130" cy="36" r="2"/><circle cx="162" cy="22" r="2"/><circle cx="80" cy="36" r="2"/>
    </g>
    <path d="M28 55 L184 55 L160 100 Q106 108 52 100 Z" fill="#eea435"/>
    <ellipse cx="106" cy="55" rx="78" ry="7" fill="#f5b650"/>
    <text x="106" y="86" fill="#fff" font-family="Open Sans,sans-serif" font-size="11" font-weight="600" text-anchor="middle">ROUND 1</text>
    <g fill="#e6252b"><circle cx="74" cy="120" r="2.6"/><circle cx="96" cy="125" r="2.6"/><circle cx="118" cy="120" r="3"/><circle cx="138" cy="126" r="2.6"/><circle cx="108" cy="130" r="2.4"/></g>
    <path d="M54 124 L158 124 L142 168 Q106 174 70 168 Z" fill="#c5d52a"/>
    <ellipse cx="106" cy="124" rx="52" ry="5" fill="#1aa98a"/>
    <text x="106" y="155" fill="#fff" font-family="Open Sans,sans-serif" font-size="11" font-weight="600" text-anchor="middle">ROUND 2</text>
    <g fill="#e6252b"><circle cx="94" cy="178" r="3.4"/><circle cx="106" cy="175" r="3.4"/><circle cx="118" cy="178" r="3.4"/></g>
    <path d="M84 190 L130 190 L122 218 Q107 222 92 218 Z" fill="#29a8e0"/>
    <ellipse cx="107" cy="190" rx="23" ry="3" fill="#1f78bf"/>
    <text x="107" y="209" fill="#fff" font-family="Open Sans,sans-serif" font-size="5.5" font-weight="600" text-anchor="middle">ROUND 3</text>
    <g fill="#e6252b"><circle cx="106" cy="228" r="2.8"/><circle cx="102" cy="236" r="2.8"/></g>
  </svg>
  <div class="abs heading funnel-title" style="left:306px;top:624px;color:var(--blue-deep)">Unique solutions</div>

  <div class="abs art-strip" style="top:666px" role="img" aria-label="Colourful crowd of people and technology icons illustration"></div>
</section>

<section class="flyer flyer--back">
  <div class="abs back-bg"></div>
  <div class="tab" style="top:22px;min-width:153px;background:var(--green)">How does it work?</div>
  <div class="abs heading challenge-kicker">The challenge</div>
  <div class="abs qtext">How can this factory recover water from steam instead of throwing it to the air?</div>
  <div class="abs" style="left:30px;top:135px;width:228px;height:96px;background:linear-gradient(160deg,#b9c4cc,#7b8a7c)" role="img" aria-label="Aerial photo of the factory"></div>
  <div class="abs" style="left:277px;top:58px;width:247px;height:133px;background:linear-gradient(160deg,#f1f6fb,#dde9f4)" role="img" aria-label="Process diagram of plasterboard production with steam recovery"></div>
  <div class="abs heading" style="left:277px;top:207px;width:247px;text-align:center;font-size:13px;color:var(--blue-deep)">Plasterboard manufacturing</div>

  <div class="tab" style="top:258px;min-width:153px;background:var(--blue)">Sample challenges</div>
  <div class="abs heading sub-title" style="left:30px;top:294px">Sample challenges I</div>
  <div class="abs heading sub-title" style="left:287px;top:294px">Sample challenges II</div>
  <div class="abs" style="left:264px;top:300px;width:1.5px;height:155px;background:#666"></div>

  <div class="hex-wrap" style="left:23px;top:357px;width:60px;height:53px"><div class="hex" style="left:2px;top:2px;width:56px;height:49px;background:#8aa3b8" role="img" aria-label="Cooling tower photo"></div></div>
  <div class="hex-wrap" style="left:80px;top:336px;width:60px;height:53px"><div class="hex" style="left:2px;top:2px;width:56px;height:49px;background:#a0673e" role="img" aria-label="Industrial infrastructure photo"></div></div>
  <div class="hex-wrap" style="left:136px;top:357px;width:60px;height:53px"><div class="hex" style="left:2px;top:2px;width:56px;height:49px;background:#c9a63a" role="img" aria-label="Mining vehicle photo"></div></div>
  <div class="hex-wrap" style="left:192px;top:336px;width:60px;height:53px"><div class="hex" style="left:2px;top:2px;width:56px;height:49px;background:#9a7f7a" role="img" aria-label="Building at dusk photo"></div></div>
  <div class="hex-label" style="left:53px;top:418px">Sustainability</div>
  <div class="hex-label" style="left:110px;top:397px">Infrastructure<br>costs</div>
  <div class="hex-label" style="left:166px;top:418px">Maintance<br>costs</div>
  <div class="hex-label" style="left:222px;top:397px">Service<br>Reliability</div>

  <div class="hex-wrap" style="left:278px;top:357px;width:60px;height:53px"><div class="hex" style="left:2px;top:2px;width:56px;height:49px;background:#6e8e74" role="img" aria-label="Solar panel house photo"></div></div>
  <div class="hex-wrap" style="left:336px;top:336px;width:60px;height:53px"><div class="hex" style="left:2px;top:2px;width:56px;height:49px;background:#9ab0c0" role="img" aria-label="Wind turbines photo"></div></div>
  <div class="hex-wrap" style="left:392px;top:357px;width:60px;height:53px"><div class="hex" style="left:2px;top:2px;width:56px;height:49px;background:#a7b2bd" role="img" aria-label="Factory roof photo"></div></div>
  <div class="hex-wrap" style="left:447px;top:332px;width:60px;height:53px"><div class="hex" style="left:2px;top:2px;width:56px;height:49px;background:#7e6a4c" role="img" aria-label="Workers with machinery photo"></div></div>
  <div class="hex-label" style="left:308px;top:418px">Internet<br>of Things (IoT)</div>
  <div class="hex-label" style="left:366px;top:397px">Logistics<br>costs</div>
  <div class="hex-label" style="left:422px;top:418px">Sustainability</div>
  <div class="hex-label" style="left:477px;top:393px">Labor<br>Productivity</div>

  <div class="abs community">
    <div class="divider" style="left:191px"></div>
    <div class="divider" style="left:348px"></div>
    <div class="member" style="left:113px;top:20px">
      <div class="member__photo" role="img" aria-label="Portrait photo of community solver"></div>
      <div class="member__name">Tobias</div>
      <div class="member__role">Freelance</div>
    </div>
    <div class="member" style="left:267px;top:20px">
      <div class="member__photo" role="img" aria-label="Portrait photo of community solver"></div>
      <div class="member__name">Rafael</div>
      <div class="member__role">Full Time Engineer</div>
    </div>
    <div class="member" style="left:422px;top:20px">
      <div class="member__photo" role="img" aria-label="Portrait photo of community solver"></div>
      <div class="member__name">Leyla</div>
      <div class="member__role">Engineering Student</div>
    </div>
  </div>
  <div class="tab" style="top:470px;min-width:153px;background:var(--red)">Our community</div>

  <div class="abs art-strip" style="top:690px;height:78px" role="img" aria-label="Colourful crowd of people and technology icons illustration"></div>
  <div class="abs" style="left:171px;top:668px;width:200px;height:50px;background:#fff;border-radius:4px"></div>
  <div class="abs brand" style="left:171px;top:676px;width:200px;text-align:center;font-size:19px">Quarvelent</div>
</section>

</body>
</html>
```